KTL Stewardship Powerpoint project

Hello, I would like a highly professional powerpoint design that uses the new logo that we had designed for my consulting company. I have created a starting point in powerpoint but the successful designer must take it to a new level. i would like to see a professional image on the front page as well as our website address on a banner at the bottom (www.ktlstewardship.com.au). It is going to be the document we use for presentations that will introduce my company so it must be special!

Industry/Entity Type

It Company

Requirements
Nice to have
• Some sort of design in the front page - attached is company logo for your use.

```html
<!DOCTYPE html>
<html lang="en">
<head>
<meta charset="utf-8">
<title>KTL Stewardship – Presentation Slides</title>
<link href="https://fonts.googleapis.com/css2?family=Open+Sans:wght@400;600;700&family=Quicksand:wght@500&display=swap" rel="stylesheet">
<style>
:root{
  --stage:#e7e4df;
  --blue:#2c6bb3;
  --blue-deep:#24589a;
  --blue-bright:#3a8be0;
  --ink:#1e1e1e;
  --muted:#555;
  --grey:#8a8a8a;
  --paper:#f3f3f3;
  --green:#2fa84f;
  --white:#fff;
}
*{box-sizing:border-box;margin:0;padding:0}
html,body{width:1200px;height:849px;overflow:hidden;background:var(--stage);font-family:"Open Sans",Arial,sans-serif;color:var(--ink)}
.canvas{position:relative;width:1200px;height:849px}
.slide{position:absolute;overflow:hidden;box-shadow:0 2px 6px rgba(0,0,0,.25)}
.slide--blue{background:var(--blue);color:var(--white)}
.slide--light{background:var(--paper)}
.photo-bg{position:absolute;inset:0;background:linear-gradient(135deg,#3673b8,#2a5f9f 60%,#2f6aaa)}
.photo-bg--light{background:linear-gradient(135deg,#f6f6f6,#ebebeb)}
.network-art{position:absolute;background:radial-gradient(ellipse at 40% 45%,rgba(255,255,255,.28),rgba(255,255,255,.05) 70%)}
.page-no{position:absolute;right:8px;bottom:6px;width:14px;height:14px;background:#8c9096;color:#fff;font-size:5px;display:flex;align-items:center;justify-content:center}
.wordmark{position:absolute;font-weight:700;letter-spacing:.5px;line-height:1}
.wordmark--large{font-size:24px;color:var(--white)}
.wordmark--small{font-size:7px;color:var(--blue)}
.slide-title{position:absolute;left:0;right:0;text-align:center;font-weight:700;font-size:14px}
.slide-sub{position:absolute;left:0;right:0;text-align:center;font-weight:700;font-size:7px}
.body-s{font-size:5px;line-height:1.45}
</style>
</head>
<body>
<div class="canvas">

  <!-- Slide 01: cover -->
  <section class="slide slide--blue" style="left:43px;top:19px;width:350px;height:262px">
    <div class="photo-bg" role="img" aria-label="Mosaic of smiling business people tinted in blue"></div>
    <div class="network-art" role="img" aria-label="Connected network of people icons in coloured circles" style="left:0;top:0;width:330px;height:150px"></div>
    <div class="wordmark wordmark--large" style="left:214px;top:150px;width:130px">KTL<br><span style="font-size:11px">STEWARDSHIP</span></div>
    <div class="body-s" style="position:absolute;left:222px;top:205px;font-size:6px">Name of the presenter<br>Date 00 00 00</div>
    <div style="position:absolute;left:20px;bottom:10px;font-size:5.5px">www.ktlstewardship.com.au</div>
    <div class="page-no">01</div>
  </section>

  <!-- Slide 02: slogan -->
  <section class="slide slide--blue" style="left:424px;top:19px;width:342px;height:258px">
    <div class="photo-bg" role="img" aria-label="Mosaic of smiling business people tinted in blue"></div>
    <div style="position:absolute;left:48px;top:58px;font-family:Quicksand,sans-serif;font-size:15.5px;line-height:1.18;text-align:right;width:98px">
      Add your presentation <span style="background:var(--green);padding:0 2px">Slogan</span> here and some <span style="background:var(--green);padding:0 2px">Powerful</span> things here
    </div>
    <p class="body-s" style="position:absolute;left:34px;top:180px;width:112px;text-align:justify">What we need is a template (or master) which can be varied by ourselves from case to case. Most of our cases are colorful and it's important to transport the passion of</p>
    <div role="img" aria-label="Computer monitor surrounded by social media speech bubbles" style="position:absolute;left:172px;top:60px;width:140px;height:122px;background:radial-gradient(ellipse,rgba(255,255,255,.55),rgba(255,255,255,.08) 70%);border-radius:40%"></div>
    <div class="page-no">02</div>
  </section>

  <!-- Slide 03: services -->
  <section class="slide" style="left:791px;top:19px;width:365px;height:255px;background:var(--white)">
    <div style="position:absolute;left:0;top:0;width:365px;height:165px;overflow:hidden;color:#fff">
      <div class="photo-bg" role="img" aria-label="Mosaic of smiling business people tinted in blue"></div>
      <div class="slide-title" style="top:16px;font-size:13px">Our Services in KTL Business Consulting</div>
      <div class="slide-sub" style="top:34px;font-size:6.5px">We do lorem ipsum dolor sit amet</div>
      <div style="position:absolute;top:76px;left:34px;display:flex;gap:20px">
        <div style="width:75px"><div style="font-weight:700;font-size:7px;margin-bottom:4px"><span style="display:inline-block;width:9px;height:8px;background:var(--green);margin-right:3px;vertical-align:-1px"></span>Number one</div><p class="body-s">What we need is a template (or master) which can be varied by ourselves from case to case. Most of our cases are colorful and it's important to transport the passion of</p></div>
        <div style="width:75px"><div style="font-weight:700;font-size:7px;margin-bottom:4px"><span style="display:inline-block;width:9px;height:8px;background:var(--green);margin-right:3px;vertical-align:-1px"></span>Number one</div><p class="body-s">What we need is a template (or master) which can be varied by ourselves from case to case. Most of our cases are colorful and it's important to transport the passion of</p></div>
        <div style="width:75px"><div style="font-weight:700;font-size:7px;margin-bottom:4px"><span style="display:inline-block;width:9px;height:8px;background:var(--green);margin-right:3px;vertical-align:-1px"></span>Number one</div><p class="body-s">What we need is a template (or master) which can be varied by ourselves from case to case. Most of our cases are colorful and it's important to transport the passion of</p></div>
      </div>
    </div>
    <div style="position:absolute;top:173px;left:0;right:0;text-align:center;font-size:7px;font-style:italic">Testimonials comes here</div>
    <p style="position:absolute;top:189px;left:24px;right:24px;text-align:center;font-size:5.3px;font-style:italic;line-height:1.5">" What we need is a template (or master) which can be varied by ourselves from case to case. Most of our cases are colorful and it's important to transport the passion of".<br><b style="color:var(--blue)">Followed by name of the person</b></p>
    <div class="wordmark wordmark--small" style="left:14px;top:234px">KTL<br>STEWARDSHIP</div>
    <div class="page-no">03</div>
  </section>

  <!-- Slide 04: competences -->
  <section class="slide slide--light" style="left:47px;top:292px;width:350px;height:262px">
    <div class="photo-bg photo-bg--light" role="img" aria-label="Faint mosaic of business people"></div>
    <div class="slide-title" style="top:14px">Competences of KTL Business Consulting</div>
    <div class="slide-sub" style="top:32px">We do lorem ipsum dolor sit amet</div>
    <svg style="position:absolute;left:30px;top:62px" width="310" height="60" viewBox="0 0 310 60">
      <g font-family="Open Sans, sans-serif" font-size="5.5" fill="#fff" text-anchor="middle">
        <path d="M8 8h52l16 22-16 22H8z" fill="#8a8a8a"/><circle cx="8" cy="14" r="7" fill="#fff" stroke="#aaa" stroke-width=".6"/><text x="8" y="16" fill="#333">1</text><text x="35" y="32">public</text><text x="35" y="39">relations</text>
        <path d="M86 8h52l16 22-16 22H86z" fill="var(--blue-bright)"/><circle cx="86" cy="14" r="7" fill="#fff" stroke="#aaa" stroke-width=".6"/><text x="86" y="16" fill="#333">2</text><text x="113" y="32">online PR &amp;</text><text x="113" y="39">social media</text>
        <path d="M164 8h52l16 22-16 22H164z" fill="#8a8a8a"/><circle cx="164" cy="14" r="7" fill="#fff" stroke="#aaa" stroke-width=".6"/><text x="164" y="16" fill="#333">3</text><text x="191" y="32">cross</text><text x="191" y="39">promotions</text>
        <path d="M242 8h52l16 22-16 22H242z" fill="var(--blue-bright)"/><circle cx="242" cy="14" r="7" fill="#fff" stroke="#aaa" stroke-width=".6"/><text x="242" y="16" fill="#333">4</text><text x="269" y="36">marketing</text>
      </g>
    </svg>
    <div style="position:absolute;top:152px;left:34px;display:flex;gap:9px">
      <p class="body-s" style="width:70px">Development and realization of strategic and targeted PR concepts and campaigns are our daily business: the focus is always on building trust and image for the companies, brands and their products.</p>
      <p class="body-s" style="width:70px">Digital, interactive, networked, and user-generated content. Social networks determine our everyday lives. This includes blogs, micro blogs, and social networks as well as image and video communities.</p>
      <p class="body-s" style="width:70px">We develop individual cross promotion concepts, extending them into strategic partnerships. This opens new target groups and the value transfer is beneficial for all the brands and companies involved.</p>
      <p class="body-s" style="width:70px">We realize a number of measures that accompany the PR activities: media, online and print advertising campaigns, events, POS activities, test trips, or newsletters for retail and end consumers.</p>
    </div>
    <div class="wordmark wordmark--small" style="left:14px;top:238px">KTL<br>STEWARDSHIP</div>
    <div class="page-no">04</div>
  </section>

  <!-- Slide 05: strengths -->
  <section class="slide slide--light" style="left:425px;top:296px;width:337px;height:252px">
    <div class="photo-bg photo-bg--light" role="img" aria-label="Faint mosaic of business people"></div>
    <div class="slide-title" style="top:14px;font-size:13px">Our Strength in KTL Business Consulting</div>
    <div class="slide-sub" style="top:31px;font-size:6.5px">We do lorem ipsum dolor sit amet</div>
    <svg style="position:absolute;left:108px;top:80px" width="122" height="122" viewBox="0 0 122 122">
      <circle cx="61" cy="61" r="52" fill="none" stroke="var(--blue-deep)" stroke-width="7" stroke-dasharray="20 6" transform="rotate(-170 61 61)" pathLength="260" style="stroke-dasharray:20 6 20 6 20 6 20 6 20 6 0 130"/>
      <circle cx="61" cy="61" r="52" fill="none" stroke="#9a9a9a" stroke-width="7" pathLength="260" style="stroke-dasharray:0 130 20 6 20 6 20 6 20 6 20 6" transform="rotate(-170 61 61)"/>
      <text x="61" y="58" text-anchor="middle" font-family="Open Sans, sans-serif" font-weight="700" font-size="10" fill="var(--blue)">KTL</text>
      <text x="61" y="66" text-anchor="middle" font-family="Open Sans, sans-serif" font-weight="700" font-size="5" fill="var(--blue)">STEWARDSHIP</text>
    </svg>
    <div style="position:absolute;inset:0;font-size:4.3px;line-height:1.35;color:#333">
      <div style="position:absolute;left:125px;top:62px;width:110px"><b style="color:var(--blue);font-size:5px">1. Insert your text here</b><br>Our work is individually customized and reaches the</div>
      <div style="position:absolute;left:244px;top:80px;width:85px"><b style="color:var(--blue);font-size:5px">2. Insert your text here</b><br>We guarantee customized press support in combination with press activities or DVD</div>
      <div style="position:absolute;left:248px;top:114px;width:82px"><b style="color:var(--blue);font-size:5px">3. Insert your text here</b><br>Plaid skirts are dead – long live the plaid skirts! Outdoor has long become</div>
      <div style="position:absolute;left:250px;top:152px;width:82px"><b style="color:var(--blue);font-size:5px">4. Insert your text here</b><br>Commitment, bliss, enthusiasm: all the ways to fanaticism. Athletes require the very best equipment</div>
      <div style="position:absolute;left:238px;top:197px;width:85px"><b style="color:var(--blue);font-size:5px">5. Insert your text here</b><br>Bikes, parts, accessories, equipment, apparel. Mountain biking, road</div>
      <div style="position:absolute;left:148px;top:211px;width:90px"><b style="color:var(--blue);font-size:5px">6. Insert your text here</b><br>"Lifestyle" is not simply a catchphrase to us, but a description of products</div>
      <div style="position:absolute;left:42px;top:202px;width:80px"><b style="color:var(--blue);font-size:5px">7. Insert your text here</b><br>Fashion does not exist without great emotions. Passion and feelings</div>
      <div style="position:absolute;left:20px;top:156px;width:80px"><b style="color:var(--blue);font-size:5px">8. Insert your text here</b><br>Catchword: exception. There's barely a second motorized vehicle generating</div>
      <div style="position:absolute;left:20px;top:118px;width:80px"><b style="color:var(--blue);font-size:5px">9. Insert your text here</b><br>An exciting folk market. Innovations and fashion trends need to successfully</div>
      <div style="position:absolute;left:20px;top:84px;width:80px"><b style="color:var(--blue);font-size:5px">10. Insert your text here</b><br>You can't find what you are looking for? Not all of our clients want to be</div>
    </div>
    <div class="page-no">05</div>
  </section>

  <!-- Slide 06: clients -->
  <section class="slide slide--light" style="left:793px;top:293px;width:362px;height:261px">
    <div class="photo-bg photo-bg--light" role="img" aria-label="Faint mosaic of business people"></div>
    <div class="slide-title" style="top:16px;font-size:13px">KTL Business Consulting clients</div>
    <div class="slide-sub" style="top:34px;font-size:6.5px">We do lorem ipsum dolor sit amet</div>
    <div style="position:absolute;inset:0;font-weight:700;font-size:9px;color:#222">
      <div style="position:absolute;left:42px;top:78px;display:flex;align-items:center;gap:4px"><span style="width:10px;height:10px;background:#222"></span>Strideline</div>
      <div style="position:absolute;left:140px;top:78px">Harbor Tone Media</div>
      <div style="position:absolute;left:238px;top:78px">Crestfield Pictures</div>
      <div style="position:absolute;left:0;right:0;top:122px;text-align:center;font-size:15px">Quillo</div>
      <div style="position:absolute;left:34px;top:176px">Ridgeway Gear</div>
      <div style="position:absolute;left:136px;top:176px">Summit Forge</div>
      <div style="position:absolute;left:240px;top:176px;display:flex;align-items:center;gap:4px"><span style="width:10px;height:10px;border-radius:50%;background:#222"></span>Travelock</div>
    </div>
    <div class="wordmark wordmark--small" style="left:14px;top:238px">KTL<br>STEWARDSHIP</div>
    <div class="page-no">06</div>
  </section>

  <!-- Slide 07: graphs -->
  <section class="slide slide--light" style="left:48px;top:567px;width:349px;height:262px">
    <div class="photo-bg photo-bg--light" role="img" aria-label="Faint mosaic of business people"></div>
    <div class="slide-title" style="top:16px;font-size:13px">KTL Business Consulting Graphs</div>
    <div class="slide-sub" style="top:33px;font-size:6.5px">We do lorem ipsum dolor sit amet</div>
    <svg style="position:absolute;left:12px;top:64px" width="220" height="120" viewBox="0 0 220 120" font-family="Open Sans, sans-serif" font-size="6" fill="#333">
      <g stroke="#ccc" stroke-width=".5">
        <line x1="22" y1="104" x2="215" y2="104"/><line x1="22" y1="87" x2="215" y2="87"/><line x1="22" y1="70" x2="215" y2="70"/><line x1="22" y1="53" x2="215" y2="53"/><line x1="22" y1="36" x2="215" y2="36"/><line x1="22" y1="19" x2="215" y2="19"/><line x1="22" y1="2" x2="215" y2="2"/>
      </g>
      <g text-anchor="end"><text x="16" y="106">0</text><text x="16" y="89">1</text><text x="16" y="72">2</text><text x="16" y="55">3</text><text x="16" y="38">4</text><text x="16" y="21">5</text><text x="16" y="4">6</text></g>
      <g>
        <rect x="32" y="31" width="8" height="73" fill="#7d7d7d"/><rect x="40" y="63" width="8" height="41" fill="#2f74c0"/><rect x="48" y="70" width="8" height="34" fill="#4a90e2"/>
        <rect x="80" y="61" width="8" height="43" fill="#7d7d7d"/><rect x="88" y="29" width="8" height="75" fill="#2f74c0"/><rect x="96" y="70" width="8" height="34" fill="#4a90e2"/>
        <rect x="128" y="44" width="8" height="60" fill="#7d7d7d"/><rect x="136" y="73" width="8" height="31" fill="#2f74c0"/><rect x="144" y="53" width="8" height="51" fill="#4a90e2"/>
        <rect x="176" y="27" width="8" height="77" fill="#7d7d7d"/><rect x="184" y="56" width="8" height="48" fill="#2f74c0"/><rect x="192" y="19" width="8" height="85" fill="#4a90e2"/>
      </g>
      <g text-anchor="middle"><text x="44" y="114">Category 1</text><text x="92" y="114">Category 2</text><text x="140" y="114">Category 3</text><text x="188" y="114">Category 4</text></g>
    </svg>
    <div style="position:absolute;left:238px;top:60px;width:90px;font-size:5.5px;line-height:1.5;color:#444">
      <div style="font-weight:700;font-size:7.5px;color:#888">1. Number one</div><p style="margin:3px 0 7px">What we need is a template (or master) which can be varied by ourselves from case to case.</p>
      <div style="font-weight:700;font-size:7.5px;color:var(--blue)">2. Number one</div><p style="margin:3px 0 7px">What we need is a template (or master) which can be varied by ourselves from case to case.</p>
      <div style="font-weight:700;font-size:7.5px;color:var(--blue-bright)">3. Number one</div><p style="margin-top:3px">What we need is a template (or master) which can be varied by ourselves from case to case.</p>
    </div>
    <div class="wordmark wordmark--small" style="left:14px;top:238px">KTL<br>STEWARDSHIP</div>
    <div class="page-no">07</div>
  </section>

  <!-- Slide 08: closing -->
  <section class="slide slide--blue" style="left:427px;top:561px;width:332px;height:250px">
    <div class="photo-bg" role="img" aria-label="Mosaic of smiling business people tinted in blue"></div>
    <div class="network-art" role="img" aria-label="Connected network of people icons in coloured circles" style="left:0;top:0;width:320px;height:120px"></div>
    <div style="position:absolute;left:62px;top:134px;font-weight:700;font-size:12.5px;line-height:1.45">Thanks for your<br>Attention</div>
    <div style="position:absolute;left:64px;top:180px;font-size:5.5px">www.ktlstewardship.com.au</div>
    <div style="position:absolute;left:190px;top:136px;border-left:1px solid rgba(255,255,255,.7);padding-left:6px;font-size:7px;line-height:1.45">
      <b>KTL STEWARDSHIP</b><br>Harbour Lane 14<br>Eastvale 481203<br>021-7720-1956
    </div>
    <div class="wordmark wordmark--large" style="left:12px;top:198px;font-size:20px">KTL<br><span style="font-size:9px">STEWARDSHIP</span></div>
  </section>

</div>
</body>
</html>
```